New Architectural Firm Business Cards

New Business card to compliment previous pixel forum logo (attached). Please design a business card that is simple, modern, creative....please do not use "symbols", simply the logo and associated graphics/text. The front should contain name/address/phone/email/web address (with graphics).....back should be 100% graphic design using the logo somehow. Hoping for a two color (black and yellow) design. full bleed design, no borders

Target Market(s)

Commercial Architecture Clients

Industry/Entity Type

Architecture

Contact Information for Business Card

Please design a business card that is simple, modern, creative....please do not use "symbols", simply the logo and associated graphics/text. The front should contain name/address/phone/email/web address (with graphics).....back should be 100% graphic design using the logo somehow

Font styles to use
Sans Serif

Colors
FFF300
FFF600
FEFA6F
FFFEC7
FFFEE8

Requirements
Must have
• Clean, Modern Design
Should not have
• Stock images or "icons"

```html
<!DOCTYPE html>
<html lang="en">
<head>
<meta charset="utf-8">
<title>Norvale Architecture — Business Card</title>
<link rel="stylesheet" href="https://fonts.googleapis.com/css2?family=Open+Sans:wght@400;600;700;800&display=swap">
<style>
  :root {
    --ink: #141414;
    --ink-soft: #1d1d1d;
    --paper: #ffffff;
    --stage: #e9e9e9;
    --yellow: #f6c21a;
    --text: #2a2a2a;
  }
  * { box-sizing: border-box; margin: 0; padding: 0; }
  html, body { width: 1200px; height: 900px; overflow: hidden; }
  body {
    background: var(--stage);
    font-family: "Open Sans", sans-serif;
    position: relative;
  }
  .card {
    position: absolute;
    left: 250px;
    width: 700px;
    height: 400px;
    overflow: hidden;
  }
  .card--front { top: 36px; background: var(--paper); }
  .card--back { top: 464px; background: var(--ink); }

  .front-swoosh { position: absolute; inset: 0; width: 100%; height: 100%; }

  .brand {
    position: absolute;
    left: 60px;
    top: 120px;
    width: 260px;
    text-align: center;
    color: var(--yellow);
    font-weight: 800;
    line-height: 1;
  }
  .brand__name { font-size: 52px; letter-spacing: 1px; }
  .brand__sub { font-size: 21px; letter-spacing: 2px; margin-top: 10px; }

  .divider {
    position: absolute;
    left: 350px;
    top: 70px;
    width: 2px;
    height: 200px;
    background: var(--ink);
  }

  .contact {
    position: absolute;
    left: 384px;
    top: 78px;
    color: var(--text);
  }
  .contact__name {
    font-size: 24px;
    font-weight: 800;
    color: var(--ink);
    text-transform: uppercase;
    letter-spacing: 0.5px;
  }
  .contact__role {
    font-size: 18px;
    font-weight: 600;
    color: var(--yellow);
    margin-top: 2px;
  }
  .contact__address {
    font-size: 16px;
    line-height: 1.35;
    margin-top: 16px;
  }
  .contact__list { list-style: none; margin-top: 14px; font-size: 16px; line-height: 1.5; }
  .contact__list li { display: flex; align-items: center; gap: 8px; }
  .contact__icon { width: 14px; height: 14px; flex: none; fill: var(--yellow); }

  .back-pattern {
    position: absolute;
    inset: 0;
    background: radial-gradient(ellipse at 40% 40%, #2a2a2a 0%, var(--ink-soft) 55%, var(--ink) 100%);
  }
  .back-mark {
    position: absolute;
    left: 40px;
    bottom: 36px;
    display: flex;
    align-items: center;
    gap: 10px;
    color: var(--yellow);
    font-weight: 800;
    font-size: 30px;
    letter-spacing: 1px;
  }
  .back-mark__dot { width: 14px; height: 14px; border-radius: 50%; background: var(--yellow); }
</style>
</head>
<body>

  <section class="card card--front" aria-label="Business card front">
    <svg class="front-swoosh" viewBox="0 0 700 400" preserveAspectRatio="none" aria-hidden="true">
      <path d="M0 250 C 140 330 400 380 700 385 L700 400 L0 400 Z" fill="#141414"/>
      <path d="M0 230 C 150 320 400 372 700 370 L700 386 C 420 385 160 335 0 246 Z" fill="#f6c21a"/>
      <path d="M0 224 C 150 314 400 364 700 362 L700 372 C 400 374 150 322 0 232 Z" fill="#ffffff"/>
    </svg>

    <div class="brand">
      <div class="brand__name">NORVALE</div>
      <div class="brand__sub">ARCHITECTURE</div>
    </div>

    <div class="divider"></div>

    <div class="contact">
      <h1 class="contact__name">Daniel Corrow</h1>
      <p class="contact__role">President</p>
      <p class="contact__address">1820 Harbor Crest Way<br>Bayview CA 90410</p>
      <ul class="contact__list">
        <li>
          <svg class="contact__icon" viewBox="0 0 24 24" aria-hidden="true"><path d="M6.6 10.8a15.1 15.1 0 0 0 6.6 6.6l2.2-2.2a1 1 0 0 1 1-.25 11.4 11.4 0 0 0 3.6.57 1 1 0 0 1 1 1V20a1 1 0 0 1-1 1A17 17 0 0 1 3 4a1 1 0 0 1 1-1h3.5a1 1 0 0 1 1 1c0 1.25.2 2.45.57 3.57a1 1 0 0 1-.25 1z"/></svg>
          555-010-4477
        </li>
        <li>
          <svg class="contact__icon" viewBox="0 0 24 24" aria-hidden="true"><path d="M2 5h20v14H2z M2 5l10 8 10-8" fill="none" stroke="#f6c21a" stroke-width="2.4"/></svg>
          info@norvalearch.com
        </li>
        <li>
          <svg class="contact__icon" viewBox="0 0 24 24" aria-hidden="true"><circle cx="12" cy="12" r="9" fill="none" stroke="#f6c21a" stroke-width="2.4"/><path d="M3 12h18M12 3c3 3 3 15 0 18M12 3c-3 3-3 15 0 18" fill="none" stroke="#f6c21a" stroke-width="1.8"/></svg>
          www.norvalearch.com
        </li>
      </ul>
    </div>
  </section>

  <section class="card card--back" aria-label="Business card back">
    <div class="back-pattern" role="img" aria-label="Tonal black repeating brand pattern covering the card"></div>
    <div class="back-mark">
      <span class="back-mark__dot"></span>
      NORVALE
    </div>
  </section>

</body>
</html>
```